Vault 9 Nook Storage Poster Ad

Vault 9 Nook Storage needs an 8.5" X 11" specialty storage products poster.

Graphics that illustrate seasonal tire storage, bicycle storage, and motorcycle storage.

Information on the poster will be as follows:

Tire storage: $99.00/season + tax
bicycle storage: $99.00/season + tax
motorcycle storage: $250.00/season + tax
Phone: 306-555-0148
Web: www.vault9nook.ca
Address: Vault 9 Nook Storage, 4718 Brindle Avenue, Saskatoon, SK, S4M 2J6

**Information does not need to be presented in this exact format. The designer can creatively list the services and the prices. The words phone, web, and address can be left out**

**The season that the ad is targeting is winter

Industry/Entity Type

Storage

```html
<!DOCTYPE html>
<html lang="en">
<head>
<meta charset="utf-8">
<title>Vault 9 Nook Storage – Seasonal Storage</title>
<link rel="stylesheet" href="https://fonts.googleapis.com/css2?family=Arimo:wght@700&family=Rubik+Dirt&display=swap">
<style>
  :root {
    --page-bg: #e6e6e6;
    --paper: #ffffff;
    --sky-deep: #1a5aa0;
    --sky-mid: #5b93cb;
    --snow-tint: #e8f0f8;
    --stamp-red: #c8262c;
    --price-blue: #1f9be0;
    --icon-blue: #1c5a9e;
    --navy: #1b3f7a;
  }
  * { margin: 0; padding: 0; box-sizing: border-box; }
  html, body { width: 872px; height: 1200px; overflow: hidden; }
  body {
    position: relative;
    background: var(--page-bg);
    font-family: "Arimo", Arial, sans-serif;
  }
  .poster {
    position: absolute;
    left: 16px; top: 56px;
    width: 840px; height: 1087px;
    background: var(--paper);
    border-radius: 6px;
    box-shadow: 0 4px 14px rgba(0,0,0,0.25);
    overflow: hidden;
  }
  .winter-scene {
    position: absolute;
    left: 0; top: 0;
    width: 100%; height: 380px;
    background: linear-gradient(to bottom, var(--sky-deep) 0%, var(--sky-mid) 50%, var(--snow-tint) 80%, var(--paper) 100%);
  }
  .stamp {
    position: absolute;
    left: 225px; top: 272px;
    width: 380px;
    padding: 10px 0 8px;
    transform: rotate(-8deg);
    border-top: 7px solid var(--stamp-red);
    border-bottom: 7px solid var(--stamp-red);
    text-align: center;
    font-family: "Rubik Dirt", Impact, sans-serif;
    color: var(--stamp-red);
    line-height: 0.95;
  }
  .stamp-line { display: block; font-size: 78px; letter-spacing: 1px; }
  .service {
    position: absolute;
    left: 114px;
    width: 640px; height: 100px;
    display: flex; align-items: center;
  }
  .service-art {
    width: 184px; height: 96px;
    display: flex; justify-content: center; align-items: center;
  }
  .service-art span {
    display: block;
    background: var(--icon-blue);
    border-radius: 14px;
  }
  .service--tire { top: 522px; }
  .service--bike { top: 636px; }
  .service--moto { top: 750px; }
  .service--tire .service-art span { width: 94px; height: 96px; border-radius: 47px; }
  .service--bike .service-art span { width: 172px; height: 86px; }
  .service--moto .service-art span { width: 182px; height: 90px; }
  .price {
    margin-left: 23px;
    font-size: 36px; font-weight: 700;
    color: var(--price-blue);
  }
  .brand {
    position: absolute;
    left: 0; right: 0; top: 905px;
    display: flex; justify-content: center; align-items: center; gap: 10px;
    font-size: 22px; font-weight: 700;
    color: var(--navy);
  }
  .brand-mark { width: 20px; height: 20px; background: var(--stamp-red); }
  .footer-phone {
    position: absolute;
    left: 40px; top: 975px; width: 180px;
    text-align: center;
    color: var(--price-blue);
    font-size: 20px; font-weight: 700;
  }
  .footer-address {
    position: absolute;
    left: 270px; top: 978px; width: 300px;
    text-align: center;
    color: var(--navy);
    font-size: 19px; font-weight: 700;
    line-height: 1.1;
    font-style: normal;
  }
  .footer-web {
    position: absolute;
    left: 570px; top: 975px; width: 240px;
    text-align: center;
    color: var(--price-blue);
    font-size: 20px; font-weight: 700;
  }
  .footer-icon { display: block; margin: 0 auto 8px; }
</style>
</head>
<body>
  <main class="poster">
    <div class="winter-scene" role="img" aria-label="Snowy winter scene with falling snow, large snowflakes and frosted trees"></div>

    <h1 class="stamp">
      <span class="stamp-line">SEASONAL</span>
      <span class="stamp-line">STORAGE</span>
    </h1>

    <div class="service service--tire">
      <div class="service-art"><span role="img" aria-label="Tire illustration"></span></div>
      <p class="price">$99.00/season + tax</p>
    </div>
    <div class="service service--bike">
      <div class="service-art"><span role="img" aria-label="Bicycle illustration"></span></div>
      <p class="price">$99.00/season + tax</p>
    </div>
    <div class="service service--moto">
      <div class="service-art"><span role="img" aria-label="Motorcycle illustration"></span></div>
      <p class="price">$250.00/season + tax</p>
    </div>

    <div class="brand"><span class="brand-mark"></span>Vault 9 Nook</div>

    <div class="footer-phone">
      <svg class="footer-icon" width="38" height="32" viewBox="0 0 38 32" aria-hidden="true">
        <path d="M3 10 Q19 0 35 10 L33 15 L26 13 L25 9 Q19 7 13 9 L12 13 L5 15 Z" fill="var(--navy)"/>
        <path d="M11 14 L27 14 L33 30 L5 30 Z" fill="var(--navy)"/>
        <circle cx="19" cy="22" r="5" fill="var(--paper)"/>
        <circle cx="19" cy="22" r="2" fill="var(--navy)"/>
      </svg>
      306-555-0148
    </div>

    <address class="footer-address">
      Vault 9 Nook Storage,<br>
      4718 Brindle Avenue,<br>
      Saskatoon, SK, S4M 2J6
    </address>

    <div class="footer-web">
      <svg class="footer-icon" width="34" height="32" viewBox="0 0 34 32" aria-hidden="true">
        <circle cx="17" cy="16" r="13" fill="none" stroke="var(--navy)" stroke-width="2.5"/>
        <ellipse cx="17" cy="16" rx="6" ry="13" fill="none" stroke="var(--navy)" stroke-width="1.5"/>
        <line x1="4" y1="16" x2="30" y2="16" stroke="var(--navy)" stroke-width="1.5"/>
      </svg>
      www.vault9nook.ca
    </div>
  </main>
</body>
</html>
```